Business card and stationary for Intellectual Property Consultant & Law Firm
Harborline Claims Omniworks
Business card and stationary for Intellectual Property Consultant & Law Firm - Law
Creative Brief
Simple
Dorin Makalesu
President Director
Kelor Business Center 11th Floor Jl. Raya Wibisana Kav.37-38 Jakarta Pusat 10485, Indonesia
office@harborlineclaims.example
www.harborlineclaims.example
Member: OQRU, EKLM, UVBO, WDGF
Please add Intellectual Property Rights Consultant & Law Firm for letterhead additional of our email : hbl42@harborlineclaims.example; marks@harborlineclaims.example
please add Branch office : Surabaya (+6231) 480 3926 Medan (+6261) 819 4057 Solo (+62271) 634 918
trelvorin trelvorin
Dear All, Please provide me the stationary : letterhead, envelope, cds, ballpoint, ruler, stamps, usb sticks etc
dunmoral dunmoral
Please upload Ai or eps file of your logo thankyou
Please add : Intellectual Property Rights Consultant & Law Firm in envelope and letter head.

```html
<!DOCTYPE html>
<html lang="en">
<head>
<meta charset="utf-8">
<title>Harborline Claims Omniworks – Business Card</title>
<link rel="stylesheet" href="https://fonts.googleapis.com/css2?family=Montserrat:wght@400;600;700&display=swap">
<style>
  :root {
    --backdrop: #262626;
    --card: #ffffff;
    --ink: #4a4d52;
    --ink-soft: #7a7d82;
    --accent-blue: #2a8fc9;
    --accent-orange: #f0a030;
    --band-grey: #8c8e91;
    --band-light: #d5d6d8;
  }
  * { box-sizing: border-box; margin: 0; padding: 0; }
  html, body { width: 1200px; height: 754px; overflow: hidden; }
  body {
    background: var(--backdrop);
    font-family: "Montserrat", Arial, sans-serif;
    color: var(--ink);
    position: relative;
  }
  .card {
    position: absolute;
    top: 222px;
    width: 540px;
    height: 309px;
    background: var(--card);
    overflow: hidden;
  }
  .card--front { left: 40px; }
  .card--back { left: 620px; }

  .brand {
    display: flex;
    align-items: center;
    gap: 10px;
  }
  .brand__mark {
    width: 16px; height: 16px;
    border-radius: 50%;
    background: var(--accent-blue);
    flex: none;
  }
  .brand__name {
    font-weight: 600;
    color: var(--ink);
    line-height: 1.15;
  }
  .card--front .brand {
    position: absolute;
    left: 0; right: 0; top: 118px;
    justify-content: center;
  }
  .card--front .brand__name { font-size: 24px; width: 240px; }

  .card--back .brand {
    position: absolute;
    left: 36px; top: 96px;
  }
  .card--back .brand__mark { width: 12px; height: 12px; }
  .card--back .brand__name { font-size: 17px; width: 170px; }

  .contact {
    position: absolute;
    left: 300px; top: 42px;
  }
  .contact__name {
    font-size: 12px;
    font-weight: 700;
    color: var(--accent-blue);
    text-transform: uppercase;
    letter-spacing: .5px;
  }
  .contact__title {
    font-size: 9px;
    color: var(--ink-soft);
    margin-top: 2px;
  }
  .contact__list {
    list-style: none;
    margin-top: 16px;
  }
  .contact__item {
    display: flex;
    align-items: center;
    gap: 8px;
    font-size: 9px;
    color: var(--ink);
    height: 15px;
  }
  .contact__icon { width: 10px; height: 10px; flex: none; }

  .footer-bands {
    position: absolute;
    left: 0; bottom: 0;
    width: 540px; height: 309px;
  }
  .address {
    position: absolute;
    right: 26px; bottom: 20px;
    font-size: 9px;
    color: #ffffff;
    letter-spacing: .3px;
  }
</style>
</head>
<body>

  <section class="card card--front" aria-label="Card front">
    <div class="brand">
      <span class="brand__mark"></span>
      <span class="brand__name">Harborline Claims Omniworks</span>
    </div>
  </section>

  <section class="card card--back" aria-label="Card back">
    <svg class="footer-bands" viewBox="0 0 540 309" aria-hidden="true">
      <path d="M0 238 Q300 232 540 150 L540 178 Q300 248 0 250 Z" fill="var(--accent-orange)"/>
      <path d="M0 250 Q300 248 540 178 L540 190 Q300 258 0 258 Z" fill="var(--band-light)"/>
      <path d="M0 258 Q300 258 540 190 L540 309 L0 309 Z" fill="var(--band-grey)"/>
    </svg>

    <div class="brand">
      <span class="brand__mark"></span>
      <span class="brand__name">Harborline Claims Omniworks</span>
    </div>

    <div class="contact">
      <p class="contact__name">Dorin Makalesu</p>
      <p class="contact__title">Managing Director</p>
      <ul class="contact__list">
        <li class="contact__item">
          <svg class="contact__icon" viewBox="0 0 10 10"><path d="M2 1 L4 1 L4.6 3 L3.4 3.8 Q4.2 5.8 6.2 6.6 L7 5.4 L9 6 L9 8 Q9 9 8 9 Q1 8.6 1 2 Q1 1 2 1 Z" fill="var(--ink-soft)"/></svg>
          <span>(021) 5290 4118</span>
        </li>
        <li class="contact__item">
          <svg class="contact__icon" viewBox="0 0 10 10"><rect x="1" y="2" width="8" height="6" rx="1" fill="var(--ink-soft)"/><rect x="3" y="1" width="4" height="2" fill="var(--ink-soft)"/></svg>
          <span>(021) 5290 4119</span>
        </li>
        <li class="contact__item">
          <svg class="contact__icon" viewBox="0 0 10 10"><rect x="2.5" y="0.5" width="5" height="9" rx="1" fill="var(--ink-soft)"/><circle cx="5" cy="8" r=".6" fill="#fff"/></svg>
          <span>+62 812 4410 772</span>
        </li>
        <li class="contact__item">
          <svg class="contact__icon" viewBox="0 0 10 10"><rect x="0.5" y="2" width="9" height="6" fill="var(--ink-soft)"/><path d="M0.5 2 L5 5.5 L9.5 2" fill="none" stroke="#fff" stroke-width=".8"/></svg>
          <span>office@harborlineclaims.example</span>
        </li>
        <li class="contact__item">
          <svg class="contact__icon" viewBox="0 0 10 10"><circle cx="5" cy="5" r="4.2" fill="none" stroke="var(--ink-soft)" stroke-width="1"/><path d="M1 5 H9 M5 1 Q2.5 5 5 9 M5 1 Q7.5 5 5 9" fill="none" stroke="var(--ink-soft)" stroke-width=".7"/></svg>
          <span>www.harborlineclaims.example</span>
        </li>
      </ul>
    </div>

    <p class="address">Kelor Business Center 11th Floor, Jl. Raya Wibisana Kav.37-38, Jakarta 10485</p>
  </section>

</body>
</html>
```